Business Card for Coach - ready to print

Design Business Card ready to order prints www.larsholm.coach

* An Overview / Background of the Business & Services
· Coaching
· Personal growth
* The Target Market / Audience you are trying to reach
· private person in different roles (self, familiy, business role)s
* Design Specifics; any preferences or ideas for Style, Colour, Imagery, etc
· See www.larsholm.coach
· "simple" design
· (small) element of surprise / unusual element

* Information that will be placed in the Business Card
· Beratung und Coaching
· Address: Lars Holm, Kesselgasse 7, CH-8517 Winterthur, Mobile +41 76 254 60 31
* Do you have an existing website or Facebook page where designers can learn more about your company?
· larsholm.coach

Target Market(s)

private person in different roles (self, familiy, business role)

Industry/Entity Type

Life Coaching

Contact Information for Business Card

Lars Holm
Kesselgasse 7
CH-8517 Winterthur

Mobile: +41 76 254 60 31
Email: laho@mailvale.ch
www.larsholm.coach

Font styles to use
Sans Serif

Colors

Designer to choose colors to be used in the design.

Requirements
Must have
• "simple" design
• element of surprise / unusual element
• Beratung & Coaching
• see www.larsholm.coach for colors and so...
Nice to have
• TA Symbol (three rings on top of each other) - unsual presentation
• QR Code of Website (see if it fits in and still looks good).

```html
<!DOCTYPE html>
<html lang="en">
<head>
<meta charset="utf-8">
<title>Lars Holm – Business Card</title>
<link rel="stylesheet" href="https://fonts.googleapis.com/css2?family=Oswald:wght@500&family=Work+Sans:wght@400;500&display=swap">
<style>
  :root {
    --stage: #1c1c1c;
    --card: #232323;
    --card-edge: #2c2c2c;
    --ink: #f2f2f2;
    --accent: #1a8fc4;
  }
  html, body {
    margin: 0;
    padding: 0;
    width: 1200px;
    height: 900px;
    overflow: hidden;
    background: var(--stage);
  }
  .canvas {
    position: relative;
    width: 1200px;
    height: 900px;
    display: flex;
    flex-direction: column;
    align-items: center;
    justify-content: center;
    gap: 44px;
    font-family: "Work Sans", sans-serif;
    color: var(--ink);
  }
  .card {
    position: relative;
    width: 620px;
    height: 354px;
    background: linear-gradient(135deg, var(--card) 0%, #262626 60%, #2e2e2e 100%);
    border: 1px solid var(--card-edge);
    box-shadow: 0 18px 40px rgba(0,0,0,0.55);
    box-sizing: border-box;
    overflow: hidden;
  }
  /* Back side */
  .card-back .tagline {
    position: absolute;
    left: 0;
    right: 0;
    top: 140px;
    margin: 0;
    text-align: center;
    font-weight: 500;
    font-size: 12.5px;
    line-height: 1.45;
    letter-spacing: 0.12em;
    text-transform: uppercase;
  }
  .card-back .tagline .service {
    color: var(--accent);
  }
  /* Unexpected touch: the front's divider line continues across the back edge */
  .card-back .edge-accent {
    position: absolute;
    left: 282px;
    bottom: 0;
    width: 1.5px;
    height: 90px;
    background: var(--accent);
  }
  .card-back .edge-dot {
    position: absolute;
    left: 279px;
    bottom: 88px;
    width: 7px;
    height: 7px;
    border-radius: 50%;
    background: var(--accent);
  }
  /* Front side */
  .identity {
    position: absolute;
    left: 70px;
    top: 132px;
    width: 190px;
    text-align: right;
  }
  .identity .name {
    margin: 0;
    font-family: "Oswald", sans-serif;
    font-weight: 500;
    font-size: 38px;
    line-height: 1;
    letter-spacing: 0.01em;
    color: var(--accent);
    text-transform: uppercase;
  }
  .identity .role {
    margin: 4px 6px 0 0;
    font-size: 16px;
    letter-spacing: 0.04em;
  }
  .divider {
    position: absolute;
    left: 282px;
    top: 132px;
    width: 1.5px;
    height: 66px;
    background: var(--accent);
  }
  .contacts {
    position: absolute;
    left: 306px;
    top: 140px;
    margin: 0;
    padding: 0;
    list-style: none;
    font-size: 16px;
    letter-spacing: 0.03em;
  }
  .contacts li {
    display: flex;
    align-items: center;
    gap: 10px;
    height: 23px;
  }
  .contacts svg {
    width: 11px;
    height: 11px;
    flex: none;
  }
  .address {
    position: absolute;
    left: 0;
    right: 60px;
    bottom: 40px;
    margin: 0;
    text-align: center;
    font-size: 16.5px;
    letter-spacing: 0.05em;
  }
</style>
</head>
<body>
<main class="canvas">
  <section class="card card-back" aria-label="Card back">
    <p class="tagline">Coaching / Personal Growth<br><span class="service">Beratung &amp; Coaching</span></p>
    <span class="edge-dot" aria-hidden="true"></span>
    <span class="edge-accent" aria-hidden="true"></span>
  </section>

  <section class="card card-front" aria-label="Card front">
    <div class="identity">
      <h1 class="name">Lars Holm</h1>
      <p class="role">Coach</p>
    </div>
    <div class="divider"></div>
    <ul class="contacts">
      <li>
        <svg viewBox="0 0 12 12" aria-hidden="true"><path d="M3 1 L5 3.5 L4 5 Q5 7 7 8 L8.5 7 L11 9 L9.5 11 Q4 10.5 1 3 Z" fill="var(--accent)"/></svg>
        +41 76 254 60 31
      </li>
      <li>
        <svg viewBox="0 0 12 12" aria-hidden="true"><rect x="1" y="2.5" width="10" height="7" fill="none" stroke="var(--accent)" stroke-width="1.2"/><path d="M1 2.5 L6 6.5 L11 2.5" fill="none" stroke="var(--accent)" stroke-width="1.2"/></svg>
        laho@mailvale.ch
      </li>
      <li>
        <svg viewBox="0 0 12 12" aria-hidden="true"><circle cx="6" cy="6" r="5" fill="none" stroke="var(--accent)" stroke-width="1.1"/><ellipse cx="6" cy="6" rx="2.2" ry="5" fill="none" stroke="var(--accent)" stroke-width="1"/><path d="M1 6 H11" stroke="var(--accent)" stroke-width="1"/></svg>
        www.larsholm.coach
      </li>
    </ul>
    <p class="address">Kesselgasse 7 CH-8517 Winterthur</p>
  </section>
</main>
</body>
</html>
```